Online radio: Zintavox homepage redesign

Zintavox is one of the world's leading brands of personalizable online radio -- similar to Kelvessa, but aimed at a somewhat older audience (age 35-54).

We'd like to redesign our homepage with a more contemporary look: It should emphasize our wide variety of GENRES (as the primary navigation), with the search field easy to find as a secondary navigation.

We'd like to retain our corporate color of maroon/plum. (We are not committed to the gold/yellow secondary color.)

See our current homepage at www.zintavox.com and our in-house attempt at an improved design at http://web4.zintavox.com/finder/2013ms/.

Ideally, we'd like to see designs for up to THREE different states:

(1) An initial state when users first come to the page.

(2) What the page would look like as the user is looking at channel options.

(3) What the page would look like once the media player is launched.

However, you may be able to combine (2) and (3) in a single screenshot.

Thanks!

At the request of several designers, we have decided to extend our deadline by four days. At the same time, we have increased our budget, including the addition of a 2nd place award. Thanks for your excellent work!

Reason: Extended at the request of a couple of designers. May mean you don't have to work over the weekend!

Thanks very much for your designs! We are very pleased with the overall quality of the work we are seeing. One reminder: As our brief says, the user interface "should emphasize our wide variety of GENRES (as the primary navigation), with the search field easy to find as a secondary navigation," and we feel that your design uses the SEARCH field as the primary navigation. Many of the designs use a large search field as the primary navigation. If yours does, you might want to tweak your design to put a greater emphasis on browsing genres as the primary navigation. Thanks and good luck!

Target Market(s)

Adults age 35-54 listening to online radio at work

Industry/Entity Type

Radio

Font styles to use
Sans Serif

Requirements
Must have
• This is a design/UI project -- we do not need code

```html
<!DOCTYPE html>
<html lang="en">
<head>
<meta charset="utf-8">
<title>Zintavox — Online Radio</title>
<link rel="stylesheet" href="https://fonts.googleapis.com/css2?family=Open+Sans:ital,wght@0,400;0,600;0,700;1,400&display=swap">
<style>
  :root {
    --plum: #5b0049;
    --plum-deep: #4a003b;
    --gold: #f5c400;
    --gold-line: #e8a21b;
    --page: #f2eef0;
    --ink: #222222;
    --muted: #9a9a9a;
    --rule: #cfc8cc;
    --white: #ffffff;
  }
  * { box-sizing: border-box; margin: 0; padding: 0; }
  html, body { width: 1200px; height: 941px; overflow: hidden; }
  body { font-family: "Open Sans", sans-serif; background: var(--page); position: relative; color: var(--ink); }

  .site-header {
    position: absolute; left: 0; top: 0; width: 1200px; height: 112px;
    background: var(--plum); border-bottom: 4px solid var(--gold-line);
  }
  .nav-item {
    position: absolute; top: 30px; width: 100px; margin-left: -50px;
    text-align: center; color: var(--white); font-size: 9.5px; font-weight: 600;
    text-transform: uppercase; letter-spacing: 0.1px;
  }
  .nav-item svg { display: block; margin: 0 auto 18px; width: 22px; height: 22px; }
  .nav-divider { position: absolute; top: 34px; width: 1px; height: 46px; background: rgba(255,255,255,0.08); }

  .brand {
    position: absolute; left: 508px; top: 36px; height: 38px;
    display: flex; align-items: center; gap: 6px;
  }
  .brand-dot { width: 36px; height: 36px; border-radius: 50%; background: var(--gold); }
  .brand-name { font-size: 28px; font-weight: 600; color: var(--white); letter-spacing: -0.8px; }

  .backdrop {
    position: absolute; left: 0; top: 112px; width: 1200px; height: 769px;
    background: linear-gradient(135deg, #efe9ec 0%, #f6f3f4 40%, #ece6e9 70%, #f4f0f2 100%);
  }

  .sidebar { position: absolute; left: 161px; top: 180px; width: 203px; }
  .side-search {
    height: 26px; border: 1px solid #b9b2b6; border-radius: 2px; background: rgba(255,255,255,0.6);
    display: flex; align-items: center; padding-left: 12px; gap: 10px;
    font-size: 10px; font-style: italic; color: var(--muted);
  }
  .side-list { list-style: none; margin-top: 24px; }
  .side-list li {
    height: 29px; display: flex; align-items: center; gap: 10px;
    font-size: 11px; color: var(--muted); border-bottom: 1px solid var(--rule); position: relative;
  }
  .side-list li.gap { margin-top: 16px; }
  .side-list li:last-child { border-bottom: 1px solid var(--rule); }
  .side-list svg.icon { width: 12px; height: 12px; }
  .side-list .chev {
    position: absolute; right: 0; width: 11px; height: 11px; border: 1px solid var(--muted); border-radius: 50%;
  }

  .content { position: absolute; left: 386px; top: 170px; width: 652px; }
  .headline { text-align: center; font-size: 18.5px; color: #1c1c1c; font-weight: 400; }
  .headline em { font-style: normal; color: var(--plum); }
  .station-search {
    margin: 36px auto 0; width: 352px; height: 30px; border: 1px solid #222; border-radius: 3px;
    background: var(--white); display: flex; align-items: center; padding-left: 14px; gap: 13px;
    font-size: 12.5px; color: #333;
  }

  .genres { position: absolute; left: 386px; top: 314px; width: 652px; display: grid; grid-template-columns: repeat(3, 203px); column-gap: 22.5px; row-gap: 30px; }
  .genre-tile {
    height: 131px; position: relative; display: flex; align-items: center; justify-content: center;
    color: var(--white); font-size: 20.5px; font-weight: 600; text-shadow: 0 1px 3px rgba(0,0,0,0.35);
  }
  .genre-tile .art { position: absolute; inset: 0; }
  .genre-tile span { position: relative; }
  .art-pop { background: linear-gradient(135deg, #b0138a 0%, #d62c86 50%, #c41f5f 100%); }
  .art-lite { background: linear-gradient(135deg, #9a4c8e 0%, #6e2a66 60%, #8a1d76 100%); }
  .art-country { background: linear-gradient(135deg, #7b2b54 0%, #5a1a3c 60%, #4a1431 100%); }
  .art-classical { background: linear-gradient(135deg, #8a2e57 0%, #5c1a3f 55%, #3e0f2d 100%); }
  .art-rock { background: linear-gradient(135deg, #8e3b69 0%, #5a1c48 55%, #6b2758 100%); }
  .art-jazz { background: radial-gradient(circle at 75% 20%, #b5652e 0%, #8a3536 45%, #5c1536 100%); }

  .load-more {
    position: absolute; left: 386px; top: 651px; width: 652px; height: 31px;
    background: var(--plum); border-radius: 3px; border-bottom: 2px solid var(--plum-deep);
    color: var(--white); font-size: 10.5px; font-weight: 600; text-transform: uppercase;
    display: flex; align-items: center; justify-content: center;
  }

  .site-footer { position: absolute; left: 0; top: 881px; width: 1200px; height: 60px; background: var(--plum); }
  .copyright { position: absolute; left: 161px; top: 21px; color: var(--white); font-size: 11px; }
  .social { position: absolute; top: 24px; width: 10px; height: 10px; border-radius: 50%; background: var(--gold); }
</style>
</head>
<body>
  <header class="site-header">
    <div class="nav-item" style="left:186px">
      <svg viewBox="0 0 24 24" fill="none" stroke="#f5c400" stroke-width="2.4"><path d="M5 12a7 7 0 1 0 2-5"/><path d="M3 5v4h4"/><path d="M12 8v4l3 2"/></svg>My History
    </div>
    <div class="nav-divider" style="left:228px"></div>
    <div class="nav-item" style="left:271px">
      <svg viewBox="0 0 24 24" fill="#f5c400"><path d="M12 21l-8-8a5 5 0 0 1 8-6 5 5 0 0 1 8 6z"/></svg>My Favorites
    </div>
    <div class="nav-divider" style="left:314px"></div>
    <div class="nav-item" style="left:356px">
      <svg viewBox="0 0 24 24" fill="#f5c400"><path d="M9 4l11-2v13a3 3 0 1 1-2-2.8V6l-7 1.3V17a3 3 0 1 1-2-2.8z"/></svg>Most Popular
    </div>

    <div class="brand">
      <div class="brand-dot"></div>
      <div class="brand-name">Zintavox</div>
    </div>

    <div class="nav-item" style="left:838px">
      <svg viewBox="0 0 24 24"><circle cx="12" cy="12" r="10" fill="#f5c400"/><path d="M9.5 9.5a2.5 2.5 0 1 1 3.5 2.3c-.7.4-1 .9-1 1.7" fill="none" stroke="#5b0049" stroke-width="2.2"/><circle cx="12" cy="17" r="1.3" fill="#5b0049"/></svg>Help
    </div>
    <div class="nav-divider" style="left:880px"></div>
    <div class="nav-item" style="left:923px">
      <svg viewBox="0 0 24 24" fill="none" stroke="#f5c400" stroke-width="2.4"><path d="M14 4h6v16h-6"/><path d="M3 12h11"/><path d="M10 8l4 4-4 4"/></svg>Login
    </div>
    <div class="nav-divider" style="left:966px"></div>
    <div class="nav-item" style="left:1008px">
      <svg viewBox="0 0 24 24" fill="none" stroke="#f5c400" stroke-width="2.6"><path d="M4 16v-3a8 8 0 0 1 16 0v3"/><rect x="3" y="14" width="4" height="6" rx="1" fill="#f5c400"/><rect x="17" y="14" width="4" height="6" rx="1" fill="#f5c400"/></svg>Join for Free
    </div>
  </header>

  <div class="backdrop" role="img" aria-label="Faded wall of album cover art"></div>

  <aside class="sidebar">
    <div class="side-search">
      <svg width="11" height="11" viewBox="0 0 24 24" fill="none" stroke="#888" stroke-width="3"><circle cx="10" cy="10" r="7"/><path d="M15 15l6 6"/></svg>
      Search by artist or keyword
    </div>
    <ul class="side-list">
      <li><svg class="icon" viewBox="0 0 24 24" fill="none" stroke="#9a9a9a" stroke-width="2.4"><path d="M5 12a7 7 0 1 0 2-5"/><path d="M3 5v4h4"/></svg>My History<span class="chev"></span></li>
      <li><svg class="icon" viewBox="0 0 24 24" fill="#9a9a9a"><path d="M12 21l-8-8a5 5 0 0 1 8-6 5 5 0 0 1 8 6z"/></svg>My Favorites<span class="chev"></span></li>
      <li><svg class="icon" viewBox="0 0 24 24" fill="none" stroke="#9a9a9a" stroke-width="2.6"><path d="M4 16v-3a8 8 0 0 1 16 0v3"/></svg>Most Popular<span class="chev"></span></li>
      <li class="gap"><svg class="icon" viewBox="0 0 24 24"><circle cx="12" cy="12" r="10" fill="#9a9a9a"/><circle cx="12" cy="12" r="3" fill="#eee"/></svg>Dj Picks<span class="chev"></span></li>
      <li><svg class="icon" viewBox="0 0 24 24" fill="#9a9a9a"><path d="M9 4l11-2v13a3 3 0 1 1-2-2.8V6l-7 1.3V17a3 3 0 1 1-2-2.8z"/></svg>Genres<span class="chev"></span></li>
    </ul>
  </aside>

  <main class="content">
    <h1 class="headline">Thousands of <em>radio stations</em> with endless music</h1>
    <div class="station-search">
      <svg width="12" height="12" viewBox="0 0 24 24" fill="none" stroke="#111" stroke-width="3.4"><circle cx="10" cy="10" r="7"/><path d="M15 15l6 6"/></svg>
      Find your radio station...
    </div>
  </main>

  <section class="genres">
    <div class="genre-tile"><div class="art art-pop" role="img" aria-label="Pop hits compilation artwork"></div><span>Top 40 / Pop Hits</span></div>
    <div class="genre-tile"><div class="art art-lite" role="img" aria-label="Singer portrait in plum tones"></div><span>Lite Hits</span></div>
    <div class="genre-tile"><div class="art art-country" role="img" aria-label="Acoustic guitar being played"></div><span>Country</span></div>
    <div class="genre-tile"><div class="art art-classical" role="img" aria-label="Hands on piano keys"></div><span>Classical</span></div>
    <div class="genre-tile"><div class="art art-rock" role="img" aria-label="Rock band performing on stage"></div><span>Classic Rock</span></div>
    <div class="genre-tile"><div class="art art-jazz" role="img" aria-label="Saxophone player silhouette"></div><span>Smooth Jazz</span></div>
  </section>

  <div class="load-more">Load More</div>

  <footer class="site-footer">
    <p class="copyright">Copyright © 2014 Zintavox&nbsp; - All Rights Reserved.</p>
    <span class="social" style="left:964px"></span>
    <span class="social" style="left:995px"></span>
    <span class="social" style="left:1028px"></span>
  </footer>
</body>
</html>
```